TKV Roofing Flyer/Mailer to be used to market to Homeowners

We need to create a flyer than can double as a mailer for our roofing business and possibly be used as a door hanger as well. This flyer will advertise our roofing company in a professional way with pictures as well as clear and precise text about who we are and what we offer. We are open to this flyer being a bi-fold or even a tri-fold. There would need to be an area for address if used as a mailer. A majority of our company information can be found on our website at www.tkvroofing-example.com.

Target Market(s)

Home Owners

Industry/Entity Type

Construction

Colors
0255a3
ffffff

Requirements
Must have
• Professional design, pictures, text with info regarding our company. Website: www.tkvroofing-example.com

```html
<!DOCTYPE html>
<html lang="en">
<head>
<meta charset="utf-8">
<title>TKV Roofing Door Hangers</title>
<link href="https://fonts.googleapis.com/css2?family=Oswald:wght@400;500;700&family=Roboto:wght@500&family=Montserrat:wght@600;700&family=Lora:ital@1&family=Gentium+Book+Plus&family=Cinzel:wght@700&display=swap" rel="stylesheet">
<style>
:root{
  --brand-blue:#0255a3;
  --deep-blue:#0a4fa8;
  --bright-blue:#1c72d4;
  --sky-blue:#3f8fe0;
  --white:#ffffff;
  --ink:#111418;
  --charcoal:#2b2d31;
  --stage:#3a2418;
  --grey-light:#f2f2f2;
  --grey-mid:#8c8c8c;
}
*{margin:0;padding:0;box-sizing:border-box}
html,body{width:1200px;height:991px;overflow:hidden;background:var(--stage)}
.stage{position:relative;width:1200px;height:991px}
.hanger{position:absolute;top:36px;width:335px;height:920px;overflow:hidden;background:var(--brand-blue)}
.hanger--cleaning{left:178px;background:linear-gradient(180deg,var(--bright-blue),var(--deep-blue))}
.hanger--services{left:695px;background:var(--grey-light)}
.center{position:absolute;left:0;width:100%;text-align:center;white-space:nowrap}
.headline{font-family:"Oswald",sans-serif;font-weight:700;color:var(--white);line-height:1}
.headline--small{font-size:50px}
.headline--roof{font-family:"Roboto",sans-serif;font-weight:500;font-size:104px;letter-spacing:-3px}
.headline--cleaning{font-size:64px}
.photo{position:absolute;box-shadow:0 3px 8px rgba(0,0,0,.35);border:3px solid var(--white)}
.photo--slate{left:-20px;top:480px;width:310px;height:150px;transform:rotate(-3deg);background:linear-gradient(180deg,#dfe6ee 0%,#4a5566 40%,#2c3240 100%)}
.photo--tile{left:130px;top:575px;width:240px;height:135px;transform:rotate(3deg);background:linear-gradient(180deg,#7fb2e6 0%,#a7ccee 30%,#c2583a 45%,#9a3b22 100%)}
.band-dark{position:absolute;left:0;top:730px;width:100%;height:44px;background:var(--charcoal);color:var(--white);font-family:"Montserrat",sans-serif;font-weight:700;font-size:27px;line-height:44px;text-align:center}
.band-white{position:absolute;left:0;top:774px;width:100%;height:52px;background:var(--white);border-bottom:2px solid var(--charcoal);font-family:"Lora",serif;font-style:italic;font-size:25px;line-height:52px;text-align:center;color:var(--ink)}
.contact{position:absolute;left:0;top:826px;width:100%;height:94px;background:linear-gradient(180deg,var(--white),var(--grey-mid))}
.contact__phone{top:12px;font-family:"Oswald",sans-serif;font-weight:400;font-size:33px;color:var(--ink);letter-spacing:-.5px}
.contact__web{top:60px;font-family:"Gentium Book Plus",serif;font-size:19px;color:var(--white);display:flex;justify-content:center;align-items:center;gap:4px}
.globe{width:22px;height:22px}
.services-top{position:absolute;left:0;top:0}
.brand-name{top:196px;font-family:"Cinzel",serif;font-weight:700;font-size:44px;color:var(--white)}
.services-disc{position:absolute;left:13px;top:308px;width:312px;height:312px;border-radius:50%;border:1.5px solid var(--white);background:var(--deep-blue)}
.services-blue{position:absolute;left:0;top:300px;width:100%;height:292px;background:var(--deep-blue)}
.disc-clip{position:absolute;left:0;top:0;width:100%;height:592px;overflow:hidden}
.disc-text{color:var(--white)}
.disc-text--kicker{top:412px;font-family:"Montserrat",sans-serif;font-weight:600;font-size:17px;font-weight:500}
.disc-text--title{top:440px;font-family:"Oswald",sans-serif;font-weight:700;font-size:35px;letter-spacing:.5px}
.disc-text--hours{font-family:"Gentium Book Plus",serif;font-size:30px}
.why{font-family:"Montserrat",sans-serif;font-weight:700;color:var(--ink)}
.why--lead{top:632px;font-size:29px}
.why--name{top:664px;font-size:38px}
.service-tiles{position:absolute;left:17px;top:721px;display:flex;gap:11px}
.tile{width:67px;height:67px;border-radius:3px;background:var(--brand-blue);color:var(--white);font-family:"Montserrat",sans-serif;font-weight:600;font-size:8px;line-height:1.1;text-align:center;padding-top:5px}
.tile svg{display:block;margin:4px auto 0;width:36px;height:34px}
.credentials{position:absolute;left:0;top:798px;width:100%;height:122px;background:linear-gradient(180deg,#bdbdbd,var(--grey-mid));border-top:2px solid #d0d0d0}
.credentials__line{top:9px;font-family:"Montserrat",sans-serif;font-weight:600;font-size:17px;color:var(--white);letter-spacing:.5px}
.credentials .contact__phone{top:40px}
.credentials .contact__web{top:88px}
</style>
</head>
<body>
<main class="stage">

  <section class="hanger hanger--cleaning" aria-label="Roof cleaning door hanger">
    <div class="center headline headline--small" style="top:144px">NO-BLEACH</div>
    <div class="center headline headline--small" style="top:200px">ECO-FRIENDLY</div>
    <div class="center headline headline--roof" style="top:250px">ROOF</div>
    <div class="center headline headline--cleaning" style="top:362px">CLEANING</div>
    <div class="photo photo--slate" role="img" aria-label="Photo of a dark slate roof on a house"></div>
    <div class="photo photo--tile" role="img" aria-label="Photo of a red clay tile roof under blue sky"></div>
    <div class="band-dark">YOUR ROOF IS UGLY</div>
    <div class="band-white">Don’t Replace It, Clean It!</div>
    <div class="contact">
      <div class="center contact__phone">CALL TODAY - 555-013-2468</div>
      <div class="center contact__web">
        <svg class="globe" viewBox="0 0 24 24" fill="none" stroke="#fff" stroke-width="2"><circle cx="12" cy="12" r="10"/><ellipse cx="12" cy="12" rx="4" ry="10"/><path d="M2 12h20M4 7h16M4 17h16"/></svg>
        <span>:www.tkvroofing-example.com</span>
      </div>
    </div>
  </section>

  <section class="hanger hanger--services" aria-label="Roofing services door hanger">
    <div class="services-blue"></div>
    <svg class="services-top" width="335" height="310" viewBox="0 0 335 310">
      <defs>
        <linearGradient id="topGlow" x1="0" y1="0" x2="0" y2="1">
          <stop offset="0" stop-color="#4f9be6"/><stop offset="1" stop-color="#1a66c4"/>
        </linearGradient>
      </defs>
      <polygon points="0,0 335,0 335,252 168,300 0,252" fill="url(#topGlow)"/>
      <polyline points="0,262 168,312 335,262" fill="none" stroke="#fff" stroke-width="6"/>
    </svg>
    <div class="center brand-name">TKV Roofing</div>
    <div class="disc-clip"><div class="services-disc"></div></div>
    <div class="center disc-text disc-text--kicker">RESIDENTIAL &amp; COMMERCIAL</div>
    <div class="center disc-text disc-text--title">ROOFING SERVICES</div>
    <div class="center disc-text disc-text--hours" style="top:484px">Open Monday - Saturday</div>
    <div class="center disc-text disc-text--hours" style="top:526px">8:00 AM - 8:00 PM</div>

    <div class="center why why--lead">WHY CHOOSE</div>
    <div class="center why why--name">TKV ROOFING?</div>

    <div class="service-tiles">
      <div class="tile">ROOF<br>REPAIR
        <svg viewBox="0 0 36 34" fill="none" stroke="#fff" stroke-width="2.5"><path d="M3 16 18 4l15 12"/><circle cx="18" cy="21" r="6"/><path d="M22 26l6 6"/></svg>
      </div>
      <div class="tile">ROOF<br>REPLACEMENT
        <svg viewBox="0 0 36 34" fill="#fff"><path d="M18 3 3 16h4v16h10V20h4v12h1V16h11z"/><circle cx="26" cy="26" r="7" stroke="#0255a3" stroke-width="1.5"/><path d="M26 22v8M22 26h8" stroke="#0255a3" stroke-width="2"/></svg>
      </div>
      <div class="tile">ROOF<br>DAMAGE REPAIR
        <svg viewBox="0 0 36 34" fill="#fff"><path d="M18 3 3 16h4v16h8V22h6v10h8V16h4z"/><circle cx="23" cy="13" r="5" fill="none" stroke="#fff" stroke-width="2"/></svg>
      </div>
      <div class="tile">INSURNCE<br>CLAIMS
        <svg viewBox="0 0 36 34" fill="#fff"><path d="M18 4 2 16h32z"/><rect x="5" y="17" width="26" height="15"/><rect x="9" y="21" width="5" height="5" fill="#0255a3"/><rect x="22" y="21" width="5" height="5" fill="#0255a3"/><rect x="15.5" y="23" width="5" height="9" fill="#0255a3"/></svg>
      </div>
    </div>

    <div class="credentials">
      <div class="center credentials__line">LICENSED, BONDED, &amp; INSURED</div>
      <div class="center contact__phone">CALL TODAY - 555-013-2468</div>
      <div class="center contact__web">
        <svg class="globe" viewBox="0 0 24 24" fill="none" stroke="#fff" stroke-width="2"><circle cx="12" cy="12" r="10"/><ellipse cx="12" cy="12" rx="4" ry="10"/><path d="M2 12h20M4 7h16M4 17h16"/></svg>
        <span>:www.tkvroofing-example.com</span>
      </div>
    </div>
  </section>

</main>
</body>
</html>
```